ROVN branded stationary template

We need associated stationary to accompany our new logo.

The stationary design will be used on business cards, presentation slides and document templates so needs to be provided in an EPS format so that we can adapt it. The design MUST BE ADAPTABLE.

The logo colour is #4a4195 or RGB 85/68/141. Associated colours that can be used in this stationary should compliment this colour. Other colour choices - the preference would be dark and light purples, blues, black and greys. Done how you see fit.

We want the stationary to compliment the overall design of the logo, so clean sharp lines are what we are looking for. It doesn't need to be overly intricate in design - something simple that compliments the look and feel of the logo is what we want. More focused on lines and shapes around the stationary, not any additional logos or pictures.

UK housing providers

Business

Sans Serif

• Clean sharp appearance, nothing overly elaborate.

```html
<!DOCTYPE html>
<html lang="en">
<head>
<meta charset="utf-8">
<title>ROVN business card</title>
<link rel="stylesheet" href="https://fonts.googleapis.com/css2?family=Montserrat:wght@400;600;700&display=swap">
<style>
  :root {
    --purple: #645ea8;
    --purple-deep: #4a4195;
    --paper: #ffffff;
    --paper-shade: #ececec;
    --edge-grey: #c9c9c9;
    --backdrop: #d4d4d4;
    --ink: #3a3a3a;
    --on-purple: #ffffff;
  }
  * { margin: 0; padding: 0; box-sizing: border-box; }
  html, body { width: 1200px; height: 871px; overflow: hidden; }
  body {
    background: var(--backdrop);
    font-family: "Montserrat", sans-serif;
    position: relative;
  }
  .card {
    position: absolute;
    top: 284px;
    width: 530px;
    height: 303px;
    overflow: hidden;
    box-shadow: 0 6px 18px rgba(0,0,0,0.18);
  }
  .card-front { left: 50px; background: linear-gradient(180deg, var(--paper) 0%, var(--paper-shade) 100%); }
  .card-back { left: 620px; background: var(--purple); }

  /* front */
  .info-band {
    position: absolute; left: 0; right: 0; top: 172px; height: 100px;
    background: var(--purple);
  }
  .info-band .notch {
    position: absolute; left: 44px; top: 0;
    width: 0; height: 0;
    border-left: 9px solid transparent;
    border-right: 9px solid transparent;
    border-top: 9px solid var(--paper-shade);
  }
  .edge-strip {
    position: absolute; left: 0; right: 0; bottom: 0; height: 31px;
    background: var(--edge-grey);
  }
  .brand {
    position: absolute; right: 44px; top: 40px;
    text-align: left;
  }
  .brand-row { display: flex; align-items: center; gap: 12px; }
  .brand-square { width: 26px; height: 26px; background: var(--purple-deep); }
  .brand-name {
    font-weight: 700; font-size: 48px; line-height: 1; letter-spacing: 1px;
    color: var(--purple-deep);
  }
  .brand-tagline {
    font-size: 12px; color: var(--purple); margin-top: 4px; letter-spacing: 0.3px;
  }
  .person { position: absolute; left: 30px; top: 128px; }
  .person-name { font-weight: 700; font-size: 17px; color: var(--purple-deep); letter-spacing: 0.5px; }
  .person-role { font-size: 13px; color: var(--ink); margin-top: 2px; }
  .contacts {
    position: absolute; left: 30px; top: 192px;
    list-style: none; color: var(--on-purple); font-size: 13px;
  }
  .contacts li { display: flex; align-items: center; gap: 9px; height: 21px; }
  .contacts svg { width: 14px; height: 14px; flex: none; }
  .address {
    position: absolute; right: 30px; top: 196px;
    text-align: right; color: var(--on-purple); font-size: 13px; line-height: 1.45;
  }

  /* back */
  .back-brand {
    position: absolute; left: 0; right: 0; top: 100px;
    text-align: center; color: var(--on-purple);
  }
  .back-brand .brand-row { justify-content: center; gap: 16px; }
  .back-brand .brand-square { width: 34px; height: 34px; background: var(--on-purple); }
  .back-brand .brand-name { color: var(--on-purple); font-size: 66px; }
  .back-brand .brand-tagline { color: var(--on-purple); font-size: 15px; margin-top: 8px; }
</style>
</head>
<body>

<section class="card card-front" aria-label="Business card front">
  <div class="brand">
    <div class="brand-row">
      <span class="brand-square"></span>
      <span class="brand-name">ROVN</span>
    </div>
    <div class="brand-tagline">fresh thinking for better homes</div>
  </div>

  <div class="person">
    <div class="person-name">JORDAN WHITLEY</div>
    <div class="person-role">Managing Director</div>
  </div>

  <div class="info-band"><span class="notch"></span></div>

  <ul class="contacts">
    <li>
      <svg viewBox="0 0 16 16"><rect width="16" height="16" rx="3" fill="#fff"/><path d="M5 3.5l1.8 2.2-1 1.2c.7 1.4 1.8 2.5 3.2 3.2l1.2-1 2.2 1.8-.9 1.8C7.5 12.5 3.5 8.5 3.3 4.4z" fill="#645ea8"/></svg>
      555-214-7300
    </li>
    <li>
      <svg viewBox="0 0 16 16"><rect width="16" height="16" rx="3" fill="#fff"/><rect x="5" y="3" width="6" height="4" fill="none" stroke="#645ea8" stroke-width="1.2"/><rect x="3" y="7" width="10" height="5" fill="#645ea8"/><rect x="5" y="10" width="6" height="3" fill="#fff" stroke="#645ea8" stroke-width="1"/></svg>
      555-382-1900
    </li>
    <li>
      <svg viewBox="0 0 16 16"><rect width="16" height="16" rx="3" fill="#fff"/><circle cx="8" cy="8" r="5" fill="none" stroke="#645ea8" stroke-width="1.1"/><ellipse cx="8" cy="8" rx="2.2" ry="5" fill="none" stroke="#645ea8" stroke-width="1"/><path d="M3 8h10M4 5.5h8M4 10.5h8" stroke="#645ea8" stroke-width="0.9"/></svg>
      www.ROVN.com
    </li>
  </ul>

  <div class="address">4418 Marlow Grove Rd<br>Eastbrook, CA. 90210</div>

  <div class="edge-strip"></div>
</section>

<section class="card card-back" aria-label="Business card back">
  <div class="back-brand">
    <div class="brand-row">
      <span class="brand-square"></span>
      <span class="brand-name">ROVN</span>
    </div>
    <div class="brand-tagline">fresh thinking for better homes</div>
  </div>
</section>

</body>
</html>
```